Book Cover for a technology book - The Silent Lattice

We are writing a book that is a handbook how to build a hybrid cloud - this is a technology concept where companies use cloud services both from the like of Vornix or Plenquor and also cloud services built in there own data centers - hence the term hybrid cloud. We want a book cover with the title - The Silent Lattice; which signifies that we will be teaching companies how to build a hybrid cloud that just works. We want the tagline - handbook for building Hybrid Clouds. The authors are Corwin Haddle and Ross Pelley. The cover is to be engaging and feel different than your usual technical manual. I don't have any graphics to help out however will be able to refine and tell you what I don and don't like based on your drafts. The book dimensions are yet to be determined, in the first instance it will be a PDF

Target Market(s)

technology executives and specialists

Industry/Entity Type

Information Technology

Colors

Designer to choose colors to be used in the design.

Requirements
Nice to have
• While I don't have a particular view to how it will look, I'd like the style to be more casual than ultra formal

```html
<!DOCTYPE html>
<html lang="en">
<head>
<meta charset="utf-8">
<title>The Silent Lattice — handbook for building Hybrid Clouds</title>
<link rel="stylesheet" href="https://fonts.googleapis.com/css2?family=Open+Sans:wght@700&family=Source+Code+Pro:wght@700&display=swap">
<style>
  :root {
    --paper: #ffffff;
    --ink: #0b0b0b;
    --rose: #db8aa1;
    --straw: #e6da9f;
    --sky: #8db5cf;
  }
  html, body {
    margin: 0;
    padding: 0;
    width: 848px;
    height: 1200px;
    overflow: hidden;
    background: var(--paper);
  }
  .cover {
    display: block;
    width: 848px;
    height: 1200px;
  }
  .clearing { fill: var(--paper); }
  .title, .tagline {
    font-family: "Open Sans", "Segoe UI", sans-serif;
    font-weight: 700;
    fill: var(--ink);
  }
  .title--small { font-size: 50px; }
  .title--spread { font-size: 50px; }
  .title--large { font-size: 62px; }
  .tagline { font-size: 27px; }
  .author {
    font-family: "Source Code Pro", "Consolas", monospace;
    font-weight: 700;
    font-size: 38px;
    fill: var(--ink);
  }
</style>
</head>
<body>
<svg class="cover" viewBox="0 0 1060 1500" xmlns="http://www.w3.org/2000/svg">
  <defs>
    <linearGradient id="wash" x1="0" y1="0" x2="1" y2="0">
      <stop offset="0" stop-color="#db8aa1"/>
      <stop offset="0.3" stop-color="#eee3b6"/>
      <stop offset="0.55" stop-color="#b3cde0"/>
      <stop offset="0.8" stop-color="#e7a9ba"/>
      <stop offset="1" stop-color="#8db5cf"/>
    </linearGradient>
  </defs>

  <rect class="backdrop" width="1060" height="1500" fill="url(#wash)" role="img" aria-label="Pattern of vertical stripes in rose, straw and sky blue"/>

  <g class="clearings">
    <rect class="clearing" x="290" y="641" width="510" height="152"/>
    <rect class="clearing" x="420" y="793" width="260" height="67"/>
    <rect class="clearing" x="290" y="930" width="560" height="43"/>
    <rect class="clearing" x="872" y="930" width="124" height="518"/>
  </g>

  <g class="title-block">
    <text class="title title--small" x="382" y="696" textLength="156" lengthAdjust="spacing">THE</text>
    <text class="title title--spread" x="300" y="770" textLength="340" lengthAdjust="spacing">SILENT</text>
    <text class="title title--large" x="428" y="852">LATTICE</text>
    <text class="tagline" x="301" y="960" textLength="542" lengthAdjust="spacing">handbook for building Hybrid Clouds</text>
  </g>

  <text class="author" text-anchor="middle" aria-label="Ross Pelley">
    <tspan x="901" y="966">R</tspan><tspan x="901" dy="38">O</tspan><tspan x="901" dy="38">S</tspan><tspan x="901" dy="38">S</tspan><tspan x="901" dy="38"> </tspan><tspan x="901" dy="38">P</tspan><tspan x="901" dy="38">E</tspan><tspan x="901" dy="38">L</tspan><tspan x="901" dy="38">L</tspan><tspan x="901" dy="38">E</tspan><tspan x="901" dy="38">Y</tspan>
  </text>

  <text class="author" text-anchor="middle" aria-label="Corwin Haddle">
    <tspan x="968" y="966">C</tspan><tspan x="968" dy="36">O</tspan><tspan x="968" dy="36">R</tspan><tspan x="968" dy="36">W</tspan><tspan x="968" dy="36">I</tspan><tspan x="968" dy="36">N</tspan><tspan x="968" dy="36"> </tspan><tspan x="968" dy="36">H</tspan><tspan x="968" dy="36">A</tspan><tspan x="968" dy="36">D</tspan><tspan x="968" dy="36">D</tspan><tspan x="968" dy="36">L</tspan><tspan x="968" dy="36">E</tspan>
  </text>
</svg>
</body>
</html>
```